Gentleman's grooming products require a business card

I need a business card that incorporates the logo [ or parts of ] that we had Pixel Hive design for us as uploaded.

We sell online, mens grooming products including moustache waxes, beard oils and shaving accessories.
We want a card that is classy, professional and a card that shouts mens products.

Target Market(s)

Young professional male market

Industry/Entity Type

Business

Contact Information for Business Card

Ross and Edith Carwell
Lather and Lore
Purveyors of gentleman's stiffeners and grooming requisites
M :0418529647
E : ross@latherandlore.com.au
E : edith@latherandlore.com.au
E : sales@theblokesbalmery.com.au

W : www.latherandlore.com.au

Requirements
Must have
• Class
Nice to have
• Professionalism

```html
<!DOCTYPE html>
<html lang="en">
<head>
<meta charset="utf-8">
<title>Lather and Lore — Business Card</title>
<link rel="stylesheet" href="https://fonts.googleapis.com/css2?family=Open+Sans:wght@400;600;700&display=swap">
<style>
  :root {
    --page-bg: #e9e6e1;
    --card-black: #0b0b0b;
    --card-sheen: #2a2a2a;
    --ink-white: #ffffff;
    --ink-soft: #d9d9d9;
    --rule: #bdbdbd;
  }
  * { margin: 0; padding: 0; box-sizing: border-box; }
  html, body {
    width: 1200px; height: 1022px; overflow: hidden;
    background: var(--page-bg);
    font-family: "Open Sans", Arial, sans-serif;
  }
  .stage {
    width: 1200px; height: 1022px;
    display: flex; align-items: center; justify-content: center;
  }
  .business-card {
    position: relative;
    width: 900px; height: 514px;
    border-radius: 18px;
    overflow: hidden;
    background: radial-gradient(ellipse at 38% 45%, var(--card-sheen) 0%, var(--card-black) 60%);
    box-shadow: 0 18px 40px rgba(0,0,0,0.28);
    color: var(--ink-white);
  }
  .edge-dot {
    position: absolute; top: 40px; right: -40px;
    width: 80px; height: 80px; border-radius: 50%;
    background: var(--ink-soft);
  }
  .brand-block {
    position: absolute; left: 60px; top: 140px;
    width: 340px;
  }
  .brand-row { display: flex; align-items: center; gap: 16px; }
  .brand-square {
    width: 56px; height: 56px;
    border: 2px solid var(--ink-white);
    flex: none;
  }
  .brand-name {
    font-size: 34px; font-weight: 400; letter-spacing: 0.3px;
    color: var(--ink-white); line-height: 1; white-space: nowrap;
  }
  .brand-rule {
    margin-top: 18px; height: 1px; background: var(--rule);
  }
  .brand-tagline {
    margin-top: 10px;
    font-size: 10px; line-height: 15px; letter-spacing: 1.3px; text-transform: uppercase;
    color: var(--ink-soft);
  }
  .owner-block {
    position: absolute; right: 100px; top: 56px;
    text-align: right;
  }
  .owner-name {
    font-size: 30px; font-weight: 700; color: var(--ink-white); white-space: nowrap;
  }
  .owner-company-row {
    display: flex; align-items: center; justify-content: flex-end; gap: 12px;
    margin-top: 4px;
  }
  .owner-rule { width: 210px; height: 1px; background: var(--rule); }
  .owner-company { font-size: 18px; color: var(--ink-soft); }
  .contact-block {
    position: absolute; left: 430px; bottom: 50px;
  }
  .contact-rule {
    width: 380px; height: 1px; background: var(--rule);
    margin-bottom: 14px;
  }
  .contact-list { list-style: none; }
  .contact-item {
    display: flex; align-items: center; gap: 10px;
    font-size: 19px; line-height: 30px; color: var(--ink-white); white-space: nowrap;
  }
  .contact-icon { width: 16px; height: 16px; flex: none; }
  .contact-item--web { padding-left: 26px; }
</style>
</head>
<body>
<main class="stage">
  <article class="business-card">
    <span class="edge-dot"></span>

    <header class="brand-block">
      <div class="brand-row">
        <span class="brand-square"></span>
        <span class="brand-name">Lather and Lore</span>
      </div>
      <div class="brand-rule"></div>
      <p class="brand-tagline">Purveyors of gentlemen's stiffeners and grooming requisites</p>
    </header>

    <section class="owner-block">
      <h1 class="owner-name">Ross and Edith Carwell</h1>
      <div class="owner-company-row">
        <span class="owner-rule"></span>
        <span class="owner-company">Lather and Lore</span>
      </div>
    </section>

    <section class="contact-block">
      <div class="contact-rule"></div>
      <ul class="contact-list">
        <li class="contact-item">
          <svg class="contact-icon" viewBox="0 0 16 16" aria-hidden="true"><path d="M4 1 L6.5 4.5 L5 6 C6 8.5 7.5 10 10 11 L11.5 9.5 L15 12 L13 15 C7 14.5 1.5 9 1 3 Z" fill="#fff"/></svg>
          0418 529 647
        </li>
        <li class="contact-item">
          <svg class="contact-icon" viewBox="0 0 16 16" aria-hidden="true"><rect x="1" y="3" width="14" height="10" fill="none" stroke="#fff" stroke-width="1.5"/><path d="M1 3 L8 9 L15 3" fill="none" stroke="#fff" stroke-width="1.5"/></svg>
          ross@latherandlore.com.au
        </li>
        <li class="contact-item">
          <svg class="contact-icon" viewBox="0 0 16 16" aria-hidden="true"><rect x="1" y="3" width="14" height="10" fill="none" stroke="#fff" stroke-width="1.5"/><path d="M1 3 L8 9 L15 3" fill="none" stroke="#fff" stroke-width="1.5"/></svg>
          edith@latherandlore.com.au
        </li>
        <li class="contact-item contact-item--web">sales@theblokesbalmery.com.au</li>
        <li class="contact-item contact-item--web">www.latherandlore.com.au</li>
      </ul>
    </section>
  </article>
</main>
</body>
</html>
```